Holvery Real Estate Management Consulting

To design a high end company profile that inspires confidence in high net worth individuals and similar clients. The profile to include real estate images, preferably real images. The firm is a Zambian firm and has its target to be comparable to Tesk & Company, Parlowe & Company, Wilder Osten, Lun dorv pelsin wilder osten, TLAV Real estate company as such.

Target Market(s)

Real estate clients such as high net worth individuals, private and public companies, government and international agencies, banks and insurance companies, trusts and pension funds and individual investors. the sub target market group being developers, planners, financiers, market analysts, designers, economists, engineers, architects, construction managers, quantity surveyors and public officials and others

Colors

Designer to choose colors to be used in the design.

Requirements
Must have
• Company logo

```html
<!DOCTYPE html>
<html lang="en">
<head>
<meta charset="utf-8">
<title>Holvery Real Estate – Company Profile Cover</title>
<link rel="stylesheet" href="https://fonts.googleapis.com/css2?family=Montserrat:wght@400;500;700;800&family=Roboto:wght@300;400;700;900&display=swap">
<style>
  :root{
    --backdrop:#e3e3e3;
    --ink:#0f0f11;
    --ink-soft:#1a1a1d;
    --brand-red:#d8282c;
    --grey-text:#a9a9ab;
    --white:#f2f2f2;
    --rule:rgba(255,255,255,.45);
  }
  *{margin:0;padding:0;box-sizing:border-box}
  html,body{width:1200px;height:891px;overflow:hidden;background:var(--backdrop)}
  .spread{
    position:absolute;left:75px;top:37px;width:1060px;height:747px;
    display:flex;background:var(--ink);
    font-family:"Montserrat",sans-serif;color:var(--white);
    box-shadow:0 14px 18px -10px rgba(0,0,0,.45);
  }
  .page{position:relative;width:530px;height:100%;overflow:hidden;
    background:linear-gradient(180deg,var(--ink-soft),var(--ink))}
  .page--back{box-shadow:inset -10px 0 14px -10px rgba(0,0,0,.8)}
  .world-map{position:absolute;left:20px;top:0;width:480px;height:243px;
    background:
      radial-gradient(ellipse 22% 35% at 30% 40%,rgba(70,70,74,.35),rgba(0,0,0,0) 70%),
      radial-gradient(ellipse 25% 40% at 62% 45%,rgba(70,70,74,.32),rgba(0,0,0,0) 70%),
      radial-gradient(ellipse 12% 20% at 85% 75%,rgba(70,70,74,.28),rgba(0,0,0,0) 70%)}
  .photo{position:absolute;left:0;top:243px;width:530px;height:289px}
  .photo--harbour{
    background:
      radial-gradient(ellipse 60% 10% at 40% 45%,rgba(150,80,50,.35),rgba(0,0,0,0) 80%),
      linear-gradient(180deg,#141c26 0%,#1b2530 30%,#2e2a2c 40%,#4a3128 44%,#171c22 48%,#12171d 70%,#0f1a24 76%,#0d1620 100%);
  }
  .photo--skyline{
    background:
      radial-gradient(ellipse 8% 22% at 45% 45%,rgba(255,200,120,.35),rgba(0,0,0,0) 80%),
      radial-gradient(ellipse 45% 8% at 50% 82%,rgba(255,170,90,.35),rgba(0,0,0,0) 80%),
      radial-gradient(ellipse 60% 10% at 55% 62%,rgba(190,180,160,.35),rgba(0,0,0,0) 80%),
      linear-gradient(180deg,#1f6fb0 0%,#3f85bd 26%,#8fa3b7 36%,#e0905c 43%,#2a2f3c 50%,#20263a 62%,#3a3c44 70%,#1a2436 80%,#4a4a50 90%,#22283a 100%);
  }
  .mark-square{display:block;background:var(--brand-red)}
  .emblem-frame{position:absolute;left:141px;top:95px;width:233px;height:103px;
    border:1px solid var(--rule);background:rgba(10,14,20,.3);
    display:flex;flex-direction:column;align-items:center;justify-content:center}
  .emblem-frame .mark-square{width:24px;height:24px;margin-bottom:5px}
  .brand-name{font-family:"Montserrat",sans-serif;font-weight:800;color:var(--brand-red);
    letter-spacing:.5px;text-transform:uppercase;white-space:nowrap;line-height:1.1}
  .brand-sub{font-family:"Roboto",sans-serif;font-weight:400;color:var(--grey-text);
    text-transform:uppercase;white-space:nowrap;line-height:1.1}
  .emblem-frame .brand-name{font-size:14px}
  .emblem-frame .brand-sub{font-size:6.5px;letter-spacing:.3px;margin-top:2px}
  .contact{position:absolute;left:0;width:100%;top:566px;text-align:center;
    font-family:"Roboto",sans-serif;font-weight:300;font-size:11px;line-height:1.3}
  .contact__title{margin-bottom:9px}
  .contact__firm{margin-bottom:18px}
  .contact__firm strong{color:var(--brand-red);font-weight:700}
  .contact__icons{display:flex;justify-content:center;gap:8px;margin-bottom:8px}
  .contact__line{margin-bottom:7px}
  .masthead{position:absolute;left:0;width:100%;top:85px;text-align:center}
  .masthead .mark-square{width:44px;height:44px;margin:0 auto 20px}
  .masthead .brand-name{font-size:25px}
  .masthead .brand-sub{font-size:13.5px;letter-spacing:.4px;margin-top:2px}
  .title-block{position:absolute;left:0;width:100%;top:578px;text-align:center}
  .title-block__name{font-family:"Roboto",sans-serif;font-weight:900;font-size:31px;
    color:var(--brand-red);letter-spacing:.3px;text-transform:uppercase;line-height:1}
  .title-block__line{font-family:"Roboto",sans-serif;font-weight:400;font-size:14px;
    letter-spacing:8.5px;margin-top:5px;text-transform:uppercase}
  .title-block__slogan{font-family:"Roboto",sans-serif;font-weight:300;font-size:21px;
    letter-spacing:1.5px;margin-top:33px;text-transform:uppercase}
  .title-block__web{font-family:"Roboto",sans-serif;font-size:11px;color:var(--brand-red);
    letter-spacing:3px;margin-top:25px}
</style>
</head>
<body>
  <div class="spread">
    <section class="page page--back">
      <div class="world-map" role="img" aria-label="Faint world map texture"></div>
      <div class="photo photo--harbour" role="img" aria-label="Dark dusk city skyline over a harbour">
        <div class="emblem-frame">
          <span class="mark-square" aria-hidden="true"></span>
          <span class="brand-name">Holvery Real Estate</span>
          <span class="brand-sub">Registered Property Valuation Surveyors</span>
        </div>
      </div>
      <div class="contact">
        <p class="contact__title">CONTACT US:</p>
        <p class="contact__firm">MESSRS. <strong>HRE | MANAGEMENT CONSULTING</strong></p>
        <div class="contact__icons">
          <svg width="10" height="10" viewBox="0 0 10 10" aria-hidden="true"><circle cx="5" cy="5" r="5" fill="var(--brand-red)"/><path d="M5 2.2a1.8 1.8 0 0 1 1.8 1.8C6.8 5.4 5 7.6 5 7.6S3.2 5.4 3.2 4A1.8 1.8 0 0 1 5 2.2z" fill="#111"/></svg>
          <svg width="10" height="10" viewBox="0 0 10 10" aria-hidden="true"><circle cx="5" cy="5" r="5" fill="var(--brand-red)"/><path d="M3.3 2.6l1 1-.5.7a4 4 0 0 0 1.9 1.9l.7-.5 1 1-.6.7C5 7.3 2.7 5 2.6 3.2z" fill="#111"/></svg>
          <svg width="10" height="10" viewBox="0 0 10 10" aria-hidden="true"><circle cx="5" cy="5" r="5" fill="var(--brand-red)"/><rect x="2.6" y="3.3" width="4.8" height="3.4" fill="#111"/><path d="M2.6 3.3L5 5.2 7.4 3.3" stroke="var(--brand-red)" stroke-width=".6" fill="none"/></svg>
        </div>
        <p>Unit 4 of Plot No. 2210</p>
        <p class="contact__line">Meridian Road Kafue, Lusaka</p>
        <p class="contact__line">+260 900 412 583/ 0900246810</p>
        <p>info@holverypropertyconsultants.com</p>
      </div>
    </section>
    <section class="page page--front">
      <div class="masthead">
        <span class="mark-square" aria-hidden="true"></span>
        <div class="brand-name">Holvery Real Estate</div>
        <div class="brand-sub">Registered Property Valuation Surveyors</div>
      </div>
      <div class="photo photo--skyline" role="img" aria-label="City skyline at dusk with a curved elevated railway over the water"></div>
      <div class="title-block">
        <div class="title-block__name">Holvery Real Estate</div>
        <div class="title-block__line">Management Consulting</div>
        <div class="title-block__slogan">Accelerate Success....</div>
        <div class="title-block__web">www.holveryestates.com</div>
      </div>
    </section>
  </div>
</body>
</html>
```